"The Craft of Patron Care," fourth edition cover design

Later this year, my publisher, Harold Penmarsh & Daughters, will issue a fourth, substantially revised edition of "The Craft of Patron Care," following the 2016 publication of the third edition and the second and first versions that were issued earlier.

To distinguish this new edition from previous ones, I need a cover design that visually connects and is consistent with what has preceded it, while signaling this is a new and different, worthy of prospective readers/buyers’ attention.

Attached are three different verbal approaches to the new cover; these are NOT MEANT to serve as actual designs, but rather will give you a sense of how language is to be deployed:

The first emphasizes “ART” as the key visual word in the book title;
The second emphasizes “CLIENT SERVICE” as the key visual words in the book title; and,
The third emphasizes just the word "CLIENT" in the book title.

A top-of-the-page is a pre-head that applies to all three versions:
“6 TIMELESS PRINCIPLES FOR ADVERTISING & MARKETING PRO’s
IN AN AI WORLD"

There's a mid-page sub-head for all three versions:
“THE CLASSIC GUIDE,” followed by
“FOURTH EDITION BY GERALD ASHCOMBE

And there's a one-line, bottom-of-the-page designation:
“Foreword by Mae Dunford, Global Executive Creative Director, Starbolt"

The pallette for the previously published third edition was black with red as an accent color on a field of white; I've attached a sample for reference, so you can see how it was executed. For this new fourth edition, I'd like to change the accent color from red to either Wedgewood blue, or British racing green, or an alternative that is assertive and color saturated -- think of primary colors -- that contrast sufficiently with the base of black. As an alternative, you can consider a cover that used either Wedgewood blue, British racing green, or another possibility as a full-bleed field, with copy content either revered out or surprinted.

Lastly, while the new cover largely is meant to be typographically driven, if you can come up with a visual metaphor that illustrates and builds on the book's title, that would be very helpful. By way of reference, the third edition's book cover attempted to do this by introducing a visual element at the end of the book's title that's meant to represent an artist's paint splatter (although I admit it didn't work as well as it should).

Target Market(s)

Prospective purchasers of the book who might discover copies at a bookstore, but more likely will encounter it through online distributors such as Riverdex, Hartwell & Pike, and Tindall’s.

Industry/Entity Type

Advertising and marketing

Font styles to use
Serif
Sans Serif
Other font styles liked:
• A mix of serif and san-serif typefaces is okay. for the examples I shared, I relieid on "Arial Rounded Bold" but you need not be weeded to this. If you opt to mix in a serif font, I am partial to Cambria as a typeface.

Requirements
Must have
• To achieve the goal of being “connected with but distinct” from previous editions, the new cover should be:  Largely typographic, but displaying a color palette different from the previous editions’ black-plus-red-accent on a canvas of white.  Any new accent color selected for use should be vibrant, strong, and highly saturated; think “British racing green,” “Wedgewood blue,” or their equivalents.  In addition to a powerful, “billboard” approach to type and color, consider other visual metaphors that are likely to engage the readers. The winning cover design will stand out from other books, while connecting with the previously published third edition.
Nice to have
• If you can find way to illustrate the book's title through a visual metaphor, that would be ideal.a
Should not have
• Anything that is frivolous or non-sensical

```html
<!DOCTYPE html>
<html lang="en">
<head>
<meta charset="utf-8">
<title>The Craft of Patron Care — Fourth Edition Cover</title>
<link href="https://fonts.googleapis.com/css2?family=Arimo:wght@700&family=EB+Garamond:wght@400;500;600;700&family=Noto+Serif:ital@1&display=swap" rel="stylesheet">
<style>
  :root {
    --page: #ffffff;
    --field: #1f62b8;
    --ink: #000000;
    --reverse: #ffffff;
  }
  html, body {
    margin: 0;
    padding: 0;
    width: 1200px;
    height: 1200px;
    overflow: hidden;
    background: var(--page);
  }
  .canvas {
    position: relative;
    width: 1200px;
    height: 1200px;
  }
  .cover-art {
    position: absolute;
    left: 0;
    top: 0;
    width: 1200px;
    height: 1200px;
  }
  .cover-field { fill: var(--field); }
  .prehead {
    font-family: "Arimo", Arial, sans-serif;
    font-weight: 700;
  }
  .prehead--reverse { fill: var(--reverse); }
  .prehead--ink { fill: var(--ink); }
  .title-word {
    font-family: "EB Garamond", Garamond, serif;
    font-weight: 600;
  }
  .title-word--reverse { fill: var(--reverse); }
  .title-word--ink { fill: var(--ink); }
  .subhead-guide {
    font-family: "EB Garamond", Garamond, serif;
    font-weight: 500;
    fill: var(--reverse);
  }
  .subhead-edition {
    font-family: "EB Garamond", Garamond, serif;
    font-weight: 400;
    fill: var(--ink);
  }
  .author {
    font-family: "EB Garamond", Garamond, serif;
    font-weight: 700;
    fill: var(--ink);
  }
  .foreword {
    font-family: "Noto Serif", Georgia, serif;
    font-style: italic;
    fill: var(--reverse);
  }
</style>
</head>
<body>
<main class="canvas">
  <svg class="cover-art" viewBox="0 0 1200 1200" role="img" aria-label="The Craft of Patron Care, The Classic Guide, Fourth Edition, by Gerald Ashcombe">
    <rect class="cover-field" x="240" y="60" width="720" height="1080"/>

    <text class="prehead prehead--reverse" x="289" y="124" font-size="18.5" textLength="633" lengthAdjust="spacingAndGlyphs">6 TIMELESS PRINCIPLES FOR ADVERTISING &amp; MARKETING PROS IN</text>
    <text class="prehead prehead--ink" x="514" y="151" font-size="23" textLength="180" lengthAdjust="spacingAndGlyphs">AN  A.I. WORLD</text>

    <text class="title-word title-word--reverse" transform="translate(343,408) rotate(-90)" font-size="88" textLength="170" lengthAdjust="spacingAndGlyphs">THE</text>
    <text class="title-word title-word--reverse" x="352" y="410" font-size="170" textLength="496" lengthAdjust="spacingAndGlyphs">CRAFT</text>
    <text class="title-word title-word--reverse" transform="translate(919,376) rotate(-90)" font-size="90" textLength="104" lengthAdjust="spacingAndGlyphs">OF</text>
    <text class="title-word title-word--ink" x="286" y="548" font-size="175" textLength="634" lengthAdjust="spacingAndGlyphs">PATRON</text>
    <text class="title-word title-word--reverse" x="289" y="677" font-size="170" textLength="631" lengthAdjust="spacing">CARE</text>

    <text class="subhead-guide" x="361" y="783" font-size="53" textLength="487" lengthAdjust="spacingAndGlyphs">THE CLASSIC GUIDE</text>
    <text class="subhead-edition" x="451" y="828" font-size="42" textLength="307" lengthAdjust="spacingAndGlyphs">FOURTH EDITION</text>

    <text class="author" x="433" y="1066" font-size="52" textLength="487" lengthAdjust="spacingAndGlyphs">GERALD ASHCOMBE</text>
    <text class="foreword" x="300" y="1094" font-size="19" textLength="622" lengthAdjust="spacingAndGlyphs">Foreword by Mae Dunford, Global Executive Creative Director, Starbolt</text>
  </svg>
</main>
</body>
</html>
```